Cover for "ROOTED! The skill and rhythm of guiding teams through calm and delight"

My first book for a global audience of modern performance leaders needs its cover!
I am an international executive coach and I've developed a new approach to replace classic Performance Management with a natural, sustainable approach fit for human beings :) My first book is about this approach and serves two purposes: helping leaders and sparking their curiosity to learn more, and positioning myself as a thought leader in the field.
The book is built on personal experience; it is both professional and personal ("From me to You"), and I'd like to position it beyond classic categorisation.
Its cover should communicate humanness, naturalness, ease and joy, within an unmistakably business-y context. I would like to see designs that use the color yellow (but not sure it communicates the right things).
Updates

Target Market(s)

Leaders who aspire to have a positive impact and deliver results in a meaningful way

Industry/Entity Type

Consulting & Executive Coaching - Trusted Advisor

Font styles to use
Other font styles liked:
• Helvetica Neue

Colors
0094D4
00A9DD
6FCCEA
C7EBF8
E9F6FB
FFC000
F8CF3A
FAE287
FDF2CF
FEFAEE
EE7325
F08F49
F5BC92
FAE3D3
FDF4ED

Requirements
Must have
• A both-and feeling to it (see description), e.g., masculine AND feminine, business AND humanness. Power with, not power over...
Should not have
• Too much "bling" - no classic status symbol business success language

```html
<!DOCTYPE html>
<html lang="en">
<head>
<meta charset="utf-8">
<title>Rooted — Marla Venhoven</title>
<link href="https://fonts.googleapis.com/css2?family=Bebas+Neue&family=Montserrat:wght@800&display=swap" rel="stylesheet">
<style>
  :root {
    --paper: #ffffff;
    --sun: #fdc013;
    --ink-light: #ffffff;
  }
  html, body {
    margin: 0;
    padding: 0;
    overflow: hidden;
    background: var(--paper);
  }
  .cover {
    position: relative;
    width: 854px;
    height: 1200px;
    background: var(--paper);
    overflow: hidden;
  }
  .author {
    position: absolute;
    top: 80px;
    left: 0;
    width: 100%;
    margin: 0;
    text-align: center;
    font-family: "Bebas Neue", "Arial Narrow", sans-serif;
    font-weight: 400;
    font-size: 50px;
    line-height: 50px;
    letter-spacing: 0.5em;
    padding-left: 0.5em;
    box-sizing: border-box;
    color: var(--sun);
  }
  .title {
    position: absolute;
    top: 380px;
    left: 0;
    width: 854px;
    height: 240px;
  }
  .title text {
    font-family: "Montserrat", "Helvetica Neue", sans-serif;
    font-weight: 800;
    fill: var(--sun);
  }
  .subtitle-band {
    position: absolute;
    top: 710px;
    left: 0;
    width: 100%;
    height: 382px;
    background: var(--sun);
    color: var(--ink-light);
    font-family: "Bebas Neue", "Arial Narrow", sans-serif;
  }
  .subtitle-line {
    position: absolute;
    left: 0;
    width: 100%;
    margin: 0;
    text-align: center;
    box-sizing: border-box;
    white-space: nowrap;
  }
  .subtitle-line--lead {
    top: 71px;
    font-size: 43px;
    line-height: 43px;
    letter-spacing: 0.32em;
    padding-left: 0.32em;
  }
  .subtitle-line--main {
    top: 163px;
    font-size: 63px;
    line-height: 63px;
    letter-spacing: 0.36em;
    padding-left: 0.36em;
  }
  .subtitle-line--close {
    top: 274px;
    font-size: 63px;
    line-height: 63px;
    letter-spacing: 0.17em;
    padding-left: 0.17em;
  }
  .connector {
    position: absolute;
    left: 108px;
    width: 641px;
    display: flex;
    align-items: center;
    justify-content: space-between;
  }
  .connector--of { top: 128px; }
  .connector--through { top: 234px; }
  .connector .rule {
    display: block;
    width: 252px;
    height: 3px;
    background: var(--ink-light);
  }
  .connector .word {
    font-size: 33px;
    line-height: 33px;
    letter-spacing: 0.12em;
  }
</style>
</head>
<body>
  <main class="cover">
    <p class="author">Marla Venhoven</p>

    <svg class="title" viewBox="0 0 854 240" aria-label="Rooted">
      <text x="427" y="224" text-anchor="middle" font-size="236" textLength="760" lengthAdjust="spacingAndGlyphs">ROOTED</text>
    </svg>

    <section class="subtitle-band">
      <p class="subtitle-line subtitle-line--lead">The skill and rhythm</p>
      <div class="connector connector--of">
        <span class="rule"></span><span class="word">of</span><span class="rule"></span>
      </div>
      <p class="subtitle-line subtitle-line--main">Guiding teams</p>
      <div class="connector connector--through">
        <span class="rule"></span><span class="word">through</span><span class="rule"></span>
      </div>
      <p class="subtitle-line subtitle-line--close">Calm and delight.</p>
    </section>
  </main>
</body>
</html>
```